construction company business card

I need a business card design for a new company called TK BUILDING PARTNERS. I'd like to see different designs with the name tk BUILDING PARTNERS, and others for TK Building Partners. The company field is Home Improvement and everything related with construction. Colors I like are red, blue and black. The final design should communicate/show simplicity and security.

Industry/Entity Type

Construction

Contact Information for Business Card

TK BUILDING PARTNERS
Tobias Kendrick
(555)046-7293
57-31 213th Avenue
Larkfield Hollow
10982, NY

Requirements
Must have
• HOME IMPROVEMENT

```html
<!DOCTYPE html>
<html lang="en">
<head>
<meta charset="utf-8">
<title>TK Building Partners — Business Card</title>
<link rel="stylesheet" href="https://fonts.googleapis.com/css2?family=Oswald:wght@400&family=EB+Garamond:wght@400&display=swap">
<style>
  :root {
    --card-red: #6e0000;
    --card-blue: #36489c;
    --ink-white: #ffffff;
    --ink-black: #000000;
  }
  html, body {
    margin: 0;
    padding: 0;
    width: 1200px;
    height: 702px;
    overflow: hidden;
    background: var(--card-red);
  }
  .card {
    position: relative;
    width: 1200px;
    height: 702px;
    background: var(--card-red);
    overflow: hidden;
  }
  .card__diagonal {
    position: absolute;
    inset: 0;
    width: 1200px;
    height: 702px;
  }
  .card__diagonal polygon { fill: var(--card-blue); }
  .company-name {
    position: absolute;
    left: 86px;
    top: 152px;
    margin: 0;
    font-family: "Oswald", "Arial Narrow", sans-serif;
    font-weight: 400;
    font-size: 104px;
    line-height: 1;
    letter-spacing: 1px;
    color: var(--ink-white);
    -webkit-text-stroke: 2px var(--ink-black);
    text-shadow: -4px 4px 0 var(--ink-black);
    transform: scaleX(0.74);
    transform-origin: left top;
    white-space: nowrap;
  }
  .company-name__prefix { text-transform: lowercase; }
  .tagline {
    position: absolute;
    left: 90px;
    top: 282px;
    margin: 0;
    font-family: "Oswald", "Arial Narrow", sans-serif;
    font-weight: 400;
    font-size: 30px;
    letter-spacing: 8px;
    line-height: 1;
    color: var(--ink-white);
    white-space: nowrap;
  }
  .contact {
    position: absolute;
    right: 55px;
    top: 440px;
    text-align: right;
    font-family: "EB Garamond", Garamond, serif;
    color: var(--ink-white);
    white-space: nowrap;
  }
  .contact__name {
    margin: 0 0 10px;
    font-size: 48px;
    font-weight: 400;
    line-height: 1.1;
  }
  .contact__line {
    margin: 0 0 2px;
    font-size: 35px;
    line-height: 1.25;
    letter-spacing: 0.5px;
  }
</style>
</head>
<body>
  <main class="card">
    <svg class="card__diagonal" viewBox="0 0 1200 702" aria-hidden="true">
      <polygon points="1200,94 1200,702 304,702"/>
    </svg>

    <h1 class="company-name"><span class="company-name__prefix">tk</span> BUILDING PARTNERS</h1>
    <p class="tagline">HOME IMPROVEMENT</p>

    <section class="contact">
      <p class="contact__name">Tobias Kendrick</p>
      <p class="contact__line">(555)046-7293</p>
      <p class="contact__line">57-31 213th Avenue</p>
      <p class="contact__line">Larkfield Hollow 10982, NY</p>
    </section>
  </main>
</body>
</html>
```